Premium Packaging Design for a Line of Four Beeswax Candle Scents

Need to design a beeswax quality candle design for ceramic and tube packaging. The ceramic jar size is 11oz (311g) and should be on the label with reference to hand poured or hand crafted.
4 scents that match our branding for our incense. Scents are : 1) Maple Thistle 2) Amber Fig 3) Silver Meadow 4) Cardamom Reverie. Each tube must have elements of each of its scents i.e cardamom reverie should make reference to coffee. Die Line for the candle packaging sizing is attached in files. Design is for the tube packaging only. Must include warning label on the bottom with barcode (dummy barcode can be used for design phase). Logo and other design elements can be taken from .ai incense box. Elements of bees such as wax comb or hexagonal shapes should be used.
Bottom Warning Label (text):
1) Warning Triangle should be in Yellow
2) Icons (attached should be used)
3) Wording:
Always burn within sight and never in drafty conditions
Keep away from things that catch fire
Keep away from children and pets
4) Burn Instructions
Trim wick to 1/4" each time candle is lit. Keep wax pool free of debris including matches and wick trimmings. Only burn candle on level fire resistant surface. Do not burn candle for more than 4 hours at a time.

Target Market(s)

USA market. Must have MADE IN USA on packaging

Industry/Entity Type

Health and Beauty

Font styles to use
Decorative
Script

Requirements
Must have
• Gold stamping
Nice to have
• Follow branded guidelines as per our incense box
Should not have
• cheap and generic stock images

```html
<!DOCTYPE html>
<html lang="en">
<head>
<meta charset="utf-8">
<title>Veloran Maple Thistle Candle Tube Packaging</title>
<link rel="stylesheet" href="https://fonts.googleapis.com/css2?family=Cinzel:wght@400;600;700&family=EB+Garamond:wght@400;500&display=swap">
<style>
  :root {
    --stage: #51306f;
    --lavender-deep: #5b3a8c;
    --lavender-mid: #8a6cc0;
    --lavender-light: #b7a1dd;
    --honey-wash: #c9a97a;
    --panel-purple: #6a3f93;
    --panel-purple-dark: #4d2a72;
    --label-black: #1c1a17;
    --gold: #d7b46a;
    --gold-light: #f1dc9e;
    --ink-light: #f2ecf7;
    --rim: #1e1c1f;
  }
  * { box-sizing: border-box; margin: 0; padding: 0; }
  html, body { width: 1200px; height: 529px; overflow: hidden; }
  body { background: var(--stage); font-family: "EB Garamond", serif; }

  .canvas { position: relative; width: 1200px; height: 529px; }

  /* Tube wrap panels */
  .wrap-panel {
    position: absolute;
    top: 98px;
    width: 266px;
    height: 317px;
    border-top: 14px solid var(--rim);
    overflow: hidden;
  }
  .wrap-panel--front { left: 136px; }
  .wrap-panel--back  { left: 428px; }

  .lavender-field {
    position: absolute; inset: 0;
    background:
      radial-gradient(ellipse at 30% 20%, var(--honey-wash) 0%, transparent 40%),
      radial-gradient(ellipse at 70% 70%, var(--lavender-light) 0%, transparent 55%),
      linear-gradient(160deg, var(--lavender-mid) 0%, var(--lavender-deep) 60%, var(--lavender-mid) 100%);
  }
  .lid-seam {
    position: absolute; left: 0; right: 0; top: 95px;
    height: 2px; background: rgba(30, 20, 40, 0.35);
  }

  /* Front hexagon label */
  .scent-label {
    position: absolute; left: 37px; top: 109px;
    width: 176px; height: 162px;
  }
  .scent-label svg { position: absolute; inset: 0; }
  .scent-label__text {
    position: absolute; inset: 0;
    display: flex; flex-direction: column; align-items: center;
    color: var(--gold-light); text-align: center;
  }
  .scent-label__kicker {
    margin-top: 26px;
    font-family: "Cinzel", serif; font-weight: 700;
    font-size: 7.5px; letter-spacing: 0.2px; color: #f4f0ea;
  }
  .scent-label__rule { width: 158px; height: 1px; background: var(--gold); }
  .scent-label__rule--top { margin-top: 25px; }
  .scent-label__name {
    margin: 3px 0 4px;
    font-family: "Cinzel", serif; font-weight: 400;
    font-size: 18px; line-height: 20px; color: var(--gold-light); white-space: nowrap;
  }
  .scent-label__made {
    margin-top: 25px;
    font-family: "EB Garamond", serif; font-size: 9.5px; color: #f4f0ea;
  }
  .scent-label__weight {
    margin-top: 9px;
    font-family: "EB Garamond", serif; font-size: 4.5px; color: #e9e3da;
  }

  /* Back story panel */
  .story-field {
    position: absolute; inset: 0;
    background:
      radial-gradient(ellipse at 52% 48%, var(--panel-purple) 0%, var(--panel-purple-dark) 55%, transparent 56%),
      linear-gradient(100deg, var(--lavender-mid) 0%, var(--lavender-deep) 20%, var(--panel-purple-dark) 50%, var(--lavender-deep) 80%, var(--lavender-mid) 100%);
  }
  .story-copy {
    position: absolute; left: 70px; top: 60px; width: 126px;
    font-size: 9.5px; line-height: 14.5px;
    color: var(--ink-light); text-align: center;
  }
  .story-origin {
    position: absolute; left: 0; right: 0; top: 214px;
    font-size: 9.5px; color: var(--ink-light); text-align: center;
    letter-spacing: 0.2px;
  }

  /* Lid */
  .lid {
    position: absolute; left: 708px; top: 147px;
    width: 247px; height: 275px; border-radius: 50%;
    border: 9px solid var(--rim); overflow: hidden;
  }
  .lid .lavender-field {
    background:
      radial-gradient(circle at 50% 50%, var(--lavender-light) 0%, transparent 60%),
      linear-gradient(170deg, var(--lavender-deep) 0%, var(--lavender-mid) 50%, var(--lavender-deep) 100%);
  }
  .brand-plate {
    position: absolute; left: 12px; top: 99px;
    width: 203px; height: 66px;
    background: var(--label-black);
    border: 1.5px solid var(--gold);
    display: flex; align-items: center; justify-content: center;
  }
  .brand-plate__name {
    font-family: "Cinzel", serif; font-weight: 700;
    font-size: 30px; color: var(--gold-light); letter-spacing: 0.3px;
  }
</style>
</head>
<body>
<main class="canvas">

  <section class="wrap-panel wrap-panel--front" aria-label="Front of tube">
    <div class="lavender-field" role="img" aria-label="Photograph of blooming lavender stems over a warm honey-toned wash with faint honeycomb texture"></div>
    <div class="lid-seam"></div>
    <div class="scent-label">
      <svg viewBox="0 0 176 162" width="176" height="162" aria-hidden="true">
        <polygon points="44,2 132,2 174,81 132,160 44,160 2,81" fill="var(--label-black)" stroke="var(--gold)" stroke-width="2"/>
        <polygon points="47,7 129,7 168,81 129,155 47,155 8,81" fill="none" stroke="var(--gold)" stroke-width="0.6"/>
      </svg>
      <div class="scent-label__text">
        <p class="scent-label__kicker">NATURAL BEESWAX</p>
        <div class="scent-label__rule scent-label__rule--top"></div>
        <h1 class="scent-label__name">MAPLE THISTLE</h1>
        <div class="scent-label__rule"></div>
        <p class="scent-label__made">HAND CRAFTED</p>
        <p class="scent-label__weight">NET WT. 11oz (311g)</p>
      </div>
    </div>
  </section>

  <section class="wrap-panel wrap-panel--back" aria-label="Back of tube">
    <div class="story-field" role="img" aria-label="Lavender sprigs framing a soft violet oval with a tied lavender bundle along the bottom"></div>
    <div class="lid-seam"></div>
    <p class="story-copy">Only the highest quality 100% pure American beeswax is sourced by Veloran to create our range of candles, guaranteeing sustainability. Our beeswax candles burn longer and cleaner than traditional candles, releasing a delicate blend of honey-scented fragrance that will transport your senses.</p>
    <p class="story-origin">PRODUCT OF USA</p>
  </section>

  <section class="lid" aria-label="Tube lid">
    <div class="lavender-field" role="img" aria-label="Close photograph of lavender flower heads"></div>
    <div class="brand-plate">
      <span class="brand-plate__name">VELORAN</span>
    </div>
  </section>

</main>
</body>
</html>
```